Veltrane Hand Sanitiser Spray Product Range for International Markets

Veltrane is a new Healthcare business launching a full product range of Anti-bacterial Hand Sanitiser Spray bottles in various sizes. We have a new logo which we believe differentiates us from the competition: Veltrane - Care That Goes Further
The Product Range will comprise two distinct product solution types:
- Anti-bacterial Hand Sanitisers - Alcohol based
- Anti-bacterial Hand Sanitisers - Sensitive Non Alcohol based
Bottle sizes will comprise a range containing:
100ml, 250ml, 500ml, 1ltr, 5ltr, 10ltr
Some bottles will have Pump Sprays
The Product labelling will be attractive front packaging label combined with strong product attributes and usage indicator cues.
As a Healthcare brand our logo design is light Green. We believe that this should be combined with blues and greens balanced to create contrast and strong stand-out on-shelf.
A review of competitor brands will show some similar colour cues, however as a Healthcare brand, the colour cues Green and White are synonymous with the sector. Many existing brands are very pragmatic in their label design. i.e. #it does what is says on the tin approach#. Our brand will need strong stand-out and strong aesthetic appeal too, since it will often be left in public view and around the home and office and therefore should look as attractive as possible. There will be other brand variants in the future and thought should be given to this too - with use of colour cues.
For Competitor indicators check-out the brands on Brisklot - Pine Hollow, Dermavell and others....Thank-you!

Target Market(s)

First: Female 25 - 65
Second: Male 25 - 65

Contact Information for Business Card

Garth L. Dunmore
CEO
Veltrane Healthcare Worldwide
'Care That Goes Further'
www.VeltraneHealthcare.example
E. gldunmore@veltranehealthcare.example
T. +44 7700 900318
T. +44 118 496072

Font styles to use
Sans Serif

Colors
34a7d7
33b8a4
add136
fbee3e
b768aa

```html
<!DOCTYPE html>
<html lang="en">
<head>
<meta charset="utf-8">
<title>Veltrane Hand Sanitiser Labels and Business Card</title>
<link rel="stylesheet" href="https://fonts.googleapis.com/css2?family=Montserrat:wght@400;700&display=swap">
<style>
  :root {
    --page: #f3f4f6;
    --label-deep: #1b2f8f;
    --label-mid: #2646c4;
    --label-edge: #3a5fe0;
    --white: #ffffff;
    --ink: #3c4a66;
    --ink-soft: #7b879c;
    --badge-alcohol: #f39120;
    --badge-sensitive: #3cb44a;
    --card-shadow: rgba(20, 30, 60, 0.18);
  }
  * { box-sizing: border-box; margin: 0; padding: 0; }
  html, body { width: 675px; height: 1200px; overflow: hidden; }
  body {
    background: var(--page);
    font-family: "Montserrat", Arial, sans-serif;
    position: relative;
  }

  /* Brand name placeholder: one colour, one weight */
  .brand-name {
    font-family: "Montserrat", Arial, sans-serif;
    font-weight: 700;
    color: var(--white);
    letter-spacing: 0.5px;
    line-height: 1;
  }

  /* Product labels */
  .label-row {
    position: absolute;
    top: 150px;
    left: 0;
    width: 675px;
    display: flex;
    justify-content: center;
    gap: 40px;
  }
  .product-label {
    width: 270px;
    height: 330px;
    background: linear-gradient(90deg, var(--label-deep) 0%, var(--label-mid) 45%, var(--label-edge) 55%, var(--label-deep) 100%);
    display: flex;
    flex-direction: column;
    align-items: center;
    padding-top: 84px;
    box-shadow: 0 10px 24px var(--card-shadow);
  }
  .product-label .brand-name { font-size: 30px; }
  .product-title {
    color: var(--white);
    font-weight: 700;
    text-align: center;
    font-size: 13px;
    line-height: 1.35;
    margin-top: 48px;
    letter-spacing: 0.3px;
  }
  .formula-badge {
    margin-top: 14px;
    padding: 5px 14px;
    color: var(--white);
    font-weight: 700;
    font-size: 9px;
    letter-spacing: 0.5px;
  }
  .formula-badge.alcohol { background: var(--badge-alcohol); }
  .formula-badge.sensitive { background: var(--badge-sensitive); }

  /* Business cards */
  .card-row {
    position: absolute;
    top: 770px;
    left: 0;
    width: 675px;
    display: flex;
    justify-content: center;
    gap: 25px;
  }
  .business-card {
    width: 300px;
    height: 180px;
    box-shadow: 0 8px 20px var(--card-shadow);
    position: relative;
  }
  .card-front {
    background: linear-gradient(135deg, var(--label-deep), var(--label-mid));
    display: flex;
    align-items: center;
    justify-content: center;
  }
  .card-front .brand-name { font-size: 32px; }
  .card-back { background: var(--white); }
  .person {
    position: absolute;
    top: 28px;
    left: 124px;
    width: 160px;
  }
  .person-name { color: var(--ink); font-size: 13px; font-weight: 400; }
  .person-role { color: var(--ink); font-size: 10px; margin-top: 2px; }
  .card-back .brand-name {
    position: absolute;
    left: 20px;
    top: 96px;
    font-size: 16px;
    color: var(--ink);
  }
  .contact {
    position: absolute;
    top: 86px;
    left: 124px;
    width: 166px;
    color: var(--ink-soft);
    font-size: 6.2px;
    line-height: 1.55;
    list-style: none;
  }
</style>
</head>
<body>
  <section class="label-row">
    <article class="product-label">
      <p class="brand-name">Veltrane</p>
      <h2 class="product-title">ANTI-BACTERIAL<br>HAND SANITIZER</h2>
      <span class="formula-badge alcohol">ALCOHOL BASED</span>
    </article>
    <article class="product-label">
      <p class="brand-name">Veltrane</p>
      <h2 class="product-title">ANTI-BACTERIAL<br>HAND SANITIZER</h2>
      <span class="formula-badge sensitive">NON ALCOHOL BASED</span>
    </article>
  </section>

  <section class="card-row">
    <div class="business-card card-front">
      <p class="brand-name">Veltrane</p>
    </div>
    <div class="business-card card-back">
      <div class="person">
        <p class="person-name">Garth L. Dunmore</p>
        <p class="person-role">CEO</p>
      </div>
      <p class="brand-name">Veltrane</p>
      <ul class="contact">
        <li>Veltrane Healthcare Worldwide</li>
        <li>'Care That Goes Further'</li>
        <li>www.VeltraneHealthcare.example</li>
        <li>E. gldunmore@veltranehealthcare.example</li>
        <li>T. +44 7700 900318</li>
        <li>T. +44 118 496072</li>
      </ul>
    </div>
  </section>
</body>
</html>
```